Awesome photographers card for an awesome new business

Double sided business card Black background and silver logo in middle on one side. Details on otherside. please keep it simple

Photographer

Gavin Tolley
0482615073
GavinTolleyPhotography82@lumenpost.com
www.GavinTolleyPhotography.com.au
Instagram _Gavin_tolley

Requirements
Must have
• My logo in Silver
• please use instagram logo instead of "Instagram"

```html
<!DOCTYPE html>
<html lang="en">
<head>
<meta charset="utf-8">
<title>Gavin Tolley Photography – Business Card</title>
<link rel="stylesheet" href="https://fonts.googleapis.com/css2?family=Lato:wght@400;700&display=swap">
<style>
  :root {
    --backdrop: #4a413b;
    --card: #24282b;
    --card-edge: #1a1d1f;
    --silver: #c9ccce;
    --text-light: #e6e8e9;
    --text-soft: #c3c7c9;
    --mark-faint: #31363a;
  }
  * { box-sizing: border-box; margin: 0; padding: 0; }
  html, body { width: 1200px; height: 780px; overflow: hidden; }
  body {
    background: var(--backdrop);
    font-family: "Lato", Arial, sans-serif;
    position: relative;
  }
  .card {
    position: absolute;
    width: 510px;
    height: 296px;
    background: var(--card);
    border-radius: 22px;
    box-shadow: 0 3px 0 var(--card-edge), 0 14px 30px rgba(0,0,0,0.35);
    overflow: hidden;
  }
  .card--front { left: 60px; top: 150px; }
  .card--back { left: 630px; top: 334px; }

  .brand-mark {
    position: absolute;
    left: 50%; top: 50%;
    width: 190px; height: 190px;
    transform: translate(-50%, -50%);
    border: 3px solid var(--silver);
    border-radius: 50%;
    display: flex; align-items: center; justify-content: center;
  }
  .brand-mark__name {
    color: var(--silver);
    font-weight: 400;
    font-size: 19px;
    letter-spacing: 3px;
    text-transform: uppercase;
  }

  .back-mark {
    position: absolute;
    right: -40px; top: 40px;
    width: 250px; height: 250px;
    border: 4px solid var(--mark-faint);
    border-radius: 50%;
    display: flex; align-items: center; justify-content: center;
  }
  .back-mark__name {
    color: var(--mark-faint);
    font-size: 24px;
    letter-spacing: 4px;
    text-transform: uppercase;
  }

  .contact {
    position: absolute;
    left: 36px; top: 58px;
    color: var(--text-soft);
  }
  .contact__name {
    color: var(--text-light);
    font-weight: 700;
    font-size: 17px;
    letter-spacing: 0.3px;
    text-transform: uppercase;
    margin-bottom: 16px;
  }
  .contact__list { list-style: none; }
  .contact__item {
    display: flex; align-items: center; gap: 7px;
    font-size: 13.5px;
    line-height: 20px;
  }
  .contact__icon { width: 14px; height: 14px; flex: none; }
  .contact__web { font-size: 13.5px; margin-top: 4px; }
</style>
</head>
<body>
  <section class="card card--front" aria-label="Card front">
    <div class="brand-mark">
      <span class="brand-mark__name">Gavin Tolley</span>
    </div>
  </section>

  <section class="card card--back" aria-label="Card back">
    <div class="back-mark" aria-hidden="true">
      <span class="back-mark__name">Gavin Tolley</span>
    </div>
    <div class="contact">
      <h1 class="contact__name">Gavin Tolley</h1>
      <ul class="contact__list">
        <li class="contact__item">
          <svg class="contact__icon" viewBox="0 0 14 14" aria-hidden="true">
            <circle cx="7" cy="7" r="7" fill="var(--text-soft)"/>
            <path d="M4.3 3.6 5.6 3.4 6.2 5 5.4 5.6Q6 7.3 8.4 8.6L9 7.8 10.6 8.4 10.4 9.7Q8.8 10.8 6 8 3.4 5.3 4.3 3.6Z" fill="var(--card)"/>
          </svg>
          0482615073
        </li>
        <li class="contact__item">
          <svg class="contact__icon" viewBox="0 0 14 14" aria-hidden="true">
            <circle cx="7" cy="7" r="7" fill="var(--text-soft)"/>
            <rect x="3.5" y="4.5" width="7" height="5" fill="none" stroke="var(--card)" stroke-width="1"/>
            <path d="M3.5 4.5 7 7.3 10.5 4.5" fill="none" stroke="var(--card)" stroke-width="1"/>
          </svg>
          GavinTolleyPhotography82@lumenpost.com
        </li>
        <li class="contact__item">
          <svg class="contact__icon" viewBox="0 0 14 14" aria-hidden="true">
            <circle cx="7" cy="7" r="7" fill="var(--text-soft)"/>
          </svg>
          Gavin_tolley
        </li>
      </ul>
      <p class="contact__web">www.GavinTolleyPhotography.com.au</p>
    </div>
  </section>
</body>
</html>
```